Easter Invitation for Harbor Grace Church

I would like a 6x9 postcard mailer inviting people to our Easter services at Harbor Grace Church in Milwaukee Wisconsin. The template is included
I would like it to be a simple invitation.
Options for wording on one side
-Easter
-Easter at Harbor Grace
-Harbor Grace This Easter
-You're Invited
We could also consider putting the date and time on this side also (Saturday, March 30th @5pm)
Side 2 would have our Logo (We do have the AI or EPS file if needed), Date, Name, Address, QR Code, phone, Website Information.
Saturday, March 30th at 5pm
Harbor Grace Church
1184 W. 37th Street
Milwaukee, WI 53208
Ph: 414-555-0172
Website: www.harborgracefold.org
tagline: A Home Where Welcomed Hearts Welcome Hearts

```html
<!DOCTYPE html>
<html lang="en">
<head>
<meta charset="utf-8">
<title>Harbor Grace Church – Easter Postcard</title>
<link href="https://fonts.googleapis.com/css2?family=Ubuntu:wght@400;500;700&family=Oswald:wght@500&display=swap" rel="stylesheet">
<style>
  :root{
    --bg:#4b4b4b;
    --red:#c20006;
    --navy:#0c0c6e;
    --blue:#2a4bd0;
    --white:#ffffff;
    --rule:#c9c9c9;
    --photo-a:#6f8fe6;
    --photo-b:#2b2a3a;
  }
  *{margin:0;padding:0;box-sizing:border-box}
  html,body{width:1200px;height:904px;overflow:hidden;background:var(--bg)}
  body{position:relative;font-family:"Ubuntu",sans-serif}
  .card{position:absolute;background:var(--white);overflow:hidden}
  .card-front{left:186px;top:58px;width:561px;height:378px}
  .card-back{left:532px;top:467px;width:482px;height:378px}
  .abs{position:absolute}
  .photo-front{left:0;top:0;width:561px;height:244px;
    background:radial-gradient(ellipse at 50% 35%,#9fc0ff 0%,var(--photo-a) 25%,#3a3f7a 60%,var(--photo-b) 100%)}
  .bands{left:0;top:0}
  .logo-name{color:var(--navy);font-weight:700;letter-spacing:-.5px;white-space:nowrap}
  .front-logo{left:20px;top:293px;font-size:26px}
  .tagline{color:var(--white);font-weight:700;text-transform:uppercase;line-height:1.2}
  .front-tagline{left:215px;top:245px;font-size:17.5px}
  .front-tagline span{display:block}
  .front-tagline span + span{padding-left:9px}
  .invite-list{left:224px;top:301px;list-style:none;color:var(--white);font-weight:700;font-size:10.5px;line-height:15px;white-space:nowrap}
  .invite-list li{display:flex;align-items:center;gap:5px}
  .invite-list li:nth-child(2){padding-left:5px}
  .invite-list li:nth-child(3){padding-left:10px}
  .invite-list li:nth-child(4){padding-left:15px}
  .dot{width:6px;height:6px;border-radius:50%;background:var(--red);flex:none}
  .date{font-family:"Oswald",sans-serif;font-weight:500;text-transform:uppercase;line-height:1.18;white-space:nowrap}
  .date-front{left:432px;top:302px;font-size:15px;color:var(--white)}
  .cal{width:34px;height:34px}
  .cal-front{left:394px;top:303px}
  .contact{color:var(--white);font-size:9px;display:flex;align-items:center;gap:5px;white-space:nowrap}
  .icon{width:11px;height:11px;flex:none}
  .front-phone{left:394px;top:341px}
  .front-web{left:394px;top:356px}
  /* back */
  .back-panel{left:0;top:0;width:270px;height:378px;background:var(--navy);
    clip-path:polygon(0 0,205px 0,263px 189px,203px 378px,0 378px)}
  .back-red{left:0;top:0;width:270px;height:97px;background:var(--red)}
  .back-daterow{left:0;top:97px;width:270px;height:57px;background:var(--white)}
  .back-rule{left:0;top:152px;width:270px;height:3px;background:var(--red)}
  .photo-back{left:0;top:158px;width:270px;height:152px;
    background:linear-gradient(180deg,#b7a9e6 0%,#8a7fb6 35%,#4a4454 70%,#2f2b30 100%)}
  .back-tagline{left:22px;top:17px;font-size:18.5px;line-height:22.5px}
  .cal-back{left:21px;top:110px}
  .date-back{left:62px;top:110px;font-size:16px;color:var(--navy)}
  .address{left:22px;top:314px;color:var(--white);font-size:9px;line-height:10.5px}
  .address .row{display:flex;gap:5px;align-items:flex-start}
  .address strong{font-weight:500}
  .back-phone{left:22px;top:349px}
  .back-web{left:22px;top:362px}
  .back-logo{left:250px;top:48px;font-size:22px}
  .stamp{left:398px;top:22px;width:63px;height:59px;border:1.5px solid var(--rule)}
  .line{height:1.5px;background:var(--rule)}
  .line-1{left:288px;top:148px;width:173px}
  .line-2{left:304px;top:188px;width:157px}
  .line-3{left:288px;top:228px;width:173px}
  .back-foot{left:215px;top:370px;width:267px;height:8px;background:var(--red)}
</style>
</head>
<body>

<section class="card card-front" aria-label="Postcard front">
  <div class="abs photo-front" role="img" aria-label="Photo of a church sanctuary with blue-lit arches, a cross and a congregation seated in rows"></div>
  <svg class="abs bands" width="561" height="378" viewBox="0 0 561 378" aria-hidden="true">
    <polygon points="188,240 561,240 561,295 205,295" fill="#c20006"/>
    <polygon points="205,295 561,295 561,378 231,378" fill="#0c0c6e"/>
    <polygon points="182,243 190,243 227,378 219,378" fill="#2a4bd0"/>
  </svg>

  <div class="abs logo-name front-logo">Harbor Grace</div>

  <h1 class="abs tagline front-tagline"><span>A Home Where</span><span>Welcomed Hearts Welcome Hearts</span></h1>

  <ul class="abs invite-list">
    <li><i class="dot"></i>Easter</li>
    <li><i class="dot"></i>Easter at Harbor Grace</li>
    <li><i class="dot"></i>Harbor Grace This Easter</li>
    <li><i class="dot"></i>You're Invited</li>
  </ul>

  <svg class="abs cal cal-front" viewBox="0 0 34 34" aria-hidden="true">
    <rect x="2" y="5" width="26" height="24" rx="3" fill="none" stroke="#c20006" stroke-width="2.4"/>
    <line x1="2" y1="11" x2="28" y2="11" stroke="#c20006" stroke-width="2.4"/>
    <line x1="9" y1="2" x2="9" y2="8" stroke="#c20006" stroke-width="2.4"/>
    <line x1="21" y1="2" x2="21" y2="8" stroke="#c20006" stroke-width="2.4"/>
    <g fill="#c20006"><rect x="6" y="15" width="3" height="3"/><rect x="11" y="15" width="3" height="3"/><rect x="6" y="20" width="3" height="3"/><rect x="11" y="20" width="3" height="3"/></g>
    <circle cx="24" cy="24" r="7.5" fill="#0c0c6e" stroke="#c20006" stroke-width="2.4"/>
    <polyline points="24,20 24,24 27,25" fill="none" stroke="#c20006" stroke-width="1.8"/>
  </svg>
  <p class="abs date date-front">Saturday,<br>March 30th at 5pm</p>

  <p class="abs contact front-phone">
    <svg class="icon" viewBox="0 0 12 12" aria-hidden="true"><circle cx="6" cy="6" r="5.3" fill="none" stroke="#c20006" stroke-width="1.2"/><path d="M4 3.3l1 1.2-.6.8c.4.8 1 1.4 1.8 1.8l.8-.6 1.2 1-.6 1C5.5 8.3 3.7 6.5 3.5 4z" fill="#c20006"/></svg>
    414-555-0172
  </p>
  <p class="abs contact front-web">
    <svg class="icon" viewBox="0 0 12 12" aria-hidden="true"><g fill="none" stroke="#c20006" stroke-width="1"><circle cx="6" cy="6" r="5.2"/><ellipse cx="6" cy="6" rx="2.3" ry="5.2"/><line x1=".8" y1="6" x2="11.2" y2="6"/></g></svg>
    www.harborgracefold.org
  </p>
</section>

<section class="card card-back" aria-label="Postcard back">
  <div class="abs back-panel">
    <div class="abs back-red"></div>
    <div class="abs back-daterow"></div>
    <div class="abs back-rule"></div>
    <div class="abs photo-back" role="img" aria-label="Photo of a full congregation seated facing the stage during a service"></div>
  </div>
  <svg class="abs bands" width="482" height="378" viewBox="0 0 482 378" aria-hidden="true">
    <polyline points="211,-2 272,189 210,380" fill="none" stroke="#0c0c6e" stroke-width="6"/>
  </svg>

  <h2 class="abs tagline back-tagline">A Home Where<br>Welcomed Hearts<br>Welcome Hearts</h2>

  <svg class="abs cal cal-back" viewBox="0 0 34 34" aria-hidden="true">
    <rect x="2" y="5" width="26" height="24" rx="3" fill="none" stroke="#c20006" stroke-width="2.4"/>
    <line x1="2" y1="11" x2="28" y2="11" stroke="#c20006" stroke-width="2.4"/>
    <line x1="9" y1="2" x2="9" y2="8" stroke="#c20006" stroke-width="2.4"/>
    <line x1="21" y1="2" x2="21" y2="8" stroke="#c20006" stroke-width="2.4"/>
    <g fill="#c20006"><rect x="6" y="15" width="3" height="3"/><rect x="11" y="15" width="3" height="3"/><rect x="6" y="20" width="3" height="3"/><rect x="11" y="20" width="3" height="3"/></g>
    <circle cx="24" cy="24" r="7.5" fill="#ffffff" stroke="#c20006" stroke-width="2.4"/>
    <polyline points="24,20 24,24 27,25" fill="none" stroke="#c20006" stroke-width="1.8"/>
  </svg>
  <p class="abs date date-back">Saturday,<br>March 30th at 5pm</p>

  <div class="abs address">
    <div class="row">
      <svg class="icon" viewBox="0 0 12 12" aria-hidden="true"><circle cx="6" cy="6" r="5.5" fill="#c20006"/><path d="M6 2.6a2 2 0 0 1 2 2c0 1.5-2 3.8-2 3.8S4 6.1 4 4.6a2 2 0 0 1 2-2z" fill="#fff"/></svg>
      <div><strong>Harbor Grace Church</strong><br>1184 W. 37th Street<br>Milwaukee, WI 53208</div>
    </div>
  </div>
  <p class="abs contact back-phone">
    <svg class="icon" viewBox="0 0 12 12" aria-hidden="true"><circle cx="6" cy="6" r="5.5" fill="#c20006"/><path d="M4 3.3l1 1.2-.6.8c.4.8 1 1.4 1.8 1.8l.8-.6 1.2 1-.6 1C5.5 8.3 3.7 6.5 3.5 4z" fill="#fff"/></svg>
    414-555-0172
  </p>
  <p class="abs contact back-web">
    <svg class="icon" viewBox="0 0 12 12" aria-hidden="true"><g fill="none" stroke="#c20006" stroke-width="1"><circle cx="6" cy="6" r="5.2"/><ellipse cx="6" cy="6" rx="2.3" ry="5.2"/><line x1=".8" y1="6" x2="11.2" y2="6"/></g></svg>
    www.harborgracefold.org
  </p>

  <div class="abs logo-name back-logo">Harbor Grace</div>
  <div class="abs stamp"></div>
  <div class="abs line line-1"></div>
  <div class="abs line line-2"></div>
  <div class="abs line line-3"></div>
  <div class="abs back-foot"></div>
</section>

</body>
</html>
```